Business Card Design Project

Name: Kunle O. Edet
Designation: Partner
Address: QRM Building, 14 Harmony Close, P.O. Box 58314, Victoria Island Lagos, Nigeria
Tel: +234 1 7395162
mobile: +234 1 7061527394
Email: koedet@larkmoorassociates.com
website www.larkmoorassociates.com

```html
<!DOCTYPE html>
<html lang="en">
<head>
<meta charset="utf-8">
<title>Larkmoor Associates – Business Card</title>
<link rel="stylesheet" href="https://fonts.googleapis.com/css2?family=Mulish:wght@400;600;700;800&display=swap">
<style>
  :root {
    --backdrop: #e4e8ea;
    --card: #ffffff;
    --ink: #3a3a3a;
    --ink-soft: #5a5a5a;
    --mint: #63dba3;
    --shadow: rgba(20, 40, 50, 0.18);
  }
  * { box-sizing: border-box; margin: 0; padding: 0; }
  html, body {
    width: 1200px;
    height: 960px;
    overflow: hidden;
  }
  body {
    background: var(--backdrop);
    font-family: "Mulish", sans-serif;
    color: var(--ink);
    display: flex;
    flex-direction: column;
    align-items: center;
    justify-content: center;
    gap: 60px;
  }
  .card {
    position: relative;
    width: 640px;
    height: 366px;
    background: var(--card);
    box-shadow: 0 8px 24px var(--shadow);
  }

  /* Front */
  .brand {
    position: absolute;
    top: 64px;
    left: 0;
    right: 0;
    display: flex;
    justify-content: center;
    align-items: center;
    gap: 18px;
  }
  .brand-square {
    width: 44px;
    height: 44px;
    background: var(--mint);
  }
  .brand-name {
    font-size: 34px;
    font-weight: 600;
    color: var(--ink);
    letter-spacing: 0.2px;
  }
  .person {
    position: absolute;
    left: 50px;
    top: 196px;
    text-align: right;
  }
  .person-name {
    font-size: 22px;
    font-weight: 700;
    color: var(--mint);
    letter-spacing: 1.2px;
    text-transform: uppercase;
  }
  .person-role {
    font-size: 17px;
    color: var(--ink-soft);
    margin-top: 2px;
  }
  .details {
    position: absolute;
    left: 320px;
    top: 176px;
    font-size: 12.5px;
    line-height: 1.4;
    color: var(--ink-soft);
  }
  .address { margin-bottom: 14px; }
  .contact {
    display: grid;
    grid-template-columns: 52px auto;
    column-gap: 4px;
  }
  .contact dt {
    font-weight: 800;
    color: var(--ink);
  }

  /* Back */
  .card-back {
    display: flex;
    align-items: center;
    justify-content: center;
  }
  .website {
    font-size: 14px;
    font-weight: 800;
    letter-spacing: 1.6px;
    color: var(--ink);
  }
</style>
</head>
<body>
  <section class="card card-front">
    <div class="brand">
      <span class="brand-square"></span>
      <span class="brand-name">Larkmoor Associates</span>
    </div>
    <div class="person">
      <p class="person-name">Kunle O. Edet</p>
      <p class="person-role">Partner</p>
    </div>
    <div class="details">
      <p class="address">QRM Building, 14 Harmony Close<br>P.O. Box 58314<br>Victoria Island Lagos, Nigeria</p>
      <dl class="contact">
        <dt>Direct:</dt><dd>+234 1 739 51 62</dd>
        <dt>Mobile:</dt><dd>+234 1 706 15 27 394</dd>
        <dt>E-mail:</dt><dd>koedet@larkmoorassociates.com</dd>
      </dl>
    </div>
  </section>

  <section class="card card-back">
    <p class="website">www.larkmoorassociates.com</p>
  </section>
</body>
</html>
```